Remodeling brochure

We need an informative homeowner friendly brochure detailing our company and things we do. We are looking for an initial setup and ideas (# of pages, etc) and then we will send more content. We are uploading our logo design. We are a high end remodeling company specializing in kitchen & bath remodels. We sell ourselves on customer communication and attention to detail in our designs and remodels.

Target Market(s)

Residential homeowners

Contact Information for Business Card

Modern and attention grabbing

Requirements
Must have
• Name- Hearth & Tile Crafters<br/>Address- 782 NW Larkspur Lane Suite #217<br/> Ankeny, Iowa 50894<br/>Phone- 515-482-7395<br/>email-htcraftersmidwest@pinemail.net

```html
<!DOCTYPE html>
<html lang="en">
<head>
<meta charset="utf-8">
<title>Hearth &amp; Tile Crafters – Folder, Brochure and Card</title>
<link rel="stylesheet" href="https://fonts.googleapis.com/css2?family=Source+Sans+3:wght@400;600;700&display=swap">
<style>
  :root {
    --brand-blue: #1a7fc6;
    --brand-blue-deep: #1570b3;
    --brand-blue-text: #1560c0;
    --paper: #ffffff;
    --backdrop: #e6e6e6;
    --ink-grey: #555b62;
    --photo-dark: #3a4556;
    --photo-mid: #6b7788;
    --photo-light: #c9cdd2;
  }
  * { box-sizing: border-box; margin: 0; padding: 0; }
  html, body { width: 1200px; height: 823px; overflow: hidden; }
  body {
    background: var(--backdrop);
    font-family: "Source Sans 3", "Helvetica Neue", Arial, sans-serif;
    position: relative;
  }

  /* Folder cover */
  .folder-cover {
    position: absolute; left: 90px; top: 170px; width: 340px; height: 450px;
    background: linear-gradient(180deg, var(--brand-blue) 0%, var(--brand-blue-deep) 100%);
    display: flex; align-items: center; justify-content: center;
  }
  .brand-lockup { display: flex; align-items: center; gap: 10px; }
  .brand-lockup__square { width: 34px; height: 34px; }
  .brand-lockup__name {
    font-weight: 600; font-size: 21px; letter-spacing: 0.5px; line-height: 1.1;
  }
  .folder-cover .brand-lockup__square { background: var(--paper); }
  .folder-cover .brand-lockup__name { color: var(--paper); }

  /* Brochure cover page */
  .brochure-page {
    position: absolute; left: 470px; top: 170px; width: 340px; height: 450px;
    background: var(--paper);
  }
  .brochure-page .brand-lockup { position: absolute; top: 34px; left: 0; right: 0; justify-content: center; }
  .brochure-page .brand-lockup__square { background: var(--brand-blue-text); width: 28px; height: 28px; }
  .brochure-page .brand-lockup__name { color: var(--brand-blue-text); font-size: 17px; }

  .hero-photo {
    position: absolute; left: 28px; top: 96px; width: 284px; height: 224px;
    border: 3px solid var(--paper);
    box-shadow: 0 1px 4px rgba(0,0,0,0.18);
    background: linear-gradient(180deg, var(--photo-mid) 0%, var(--photo-dark) 55%, var(--photo-light) 100%);
  }
  .hero-band {
    position: absolute; left: 42px; top: 176px; width: 270px; height: 60px;
    background: var(--brand-blue);
    color: var(--paper); font-weight: 700; font-size: 12.5px; line-height: 1.35;
    text-align: right; padding: 15px 12px 0 0; letter-spacing: 0.3px;
  }
  .thumb {
    position: absolute; width: 76px; height: 74px;
    border: 4px solid var(--paper);
    box-shadow: 0 1px 4px rgba(0,0,0,0.25);
  }
  .thumb--kitchen { left: 42px; top: 280px; background: linear-gradient(160deg, #4a3d33, #a08a6c); }
  .thumb--bath { left: 134px; top: 302px; background: linear-gradient(160deg, #2a2f36, #7d8590); }
  .thumb--room { left: 226px; top: 292px; background: linear-gradient(160deg, #5f7c86, #b9c8cc); }
  .brochure-page__url {
    position: absolute; left: 0; right: 0; bottom: 26px;
    text-align: center; font-size: 10px; color: var(--ink-grey); letter-spacing: 0.2px;
  }

  /* Business card */
  .business-card {
    position: absolute; left: 850px; top: 395px; width: 260px; height: 140px;
    background: var(--paper);
    box-shadow: 0 1px 4px rgba(0,0,0,0.15);
    padding: 16px 18px; color: var(--ink-grey);
  }
  .business-card__name { font-size: 11px; text-transform: uppercase; letter-spacing: 0.2px; }
  .business-card__role { font-size: 7px; text-transform: uppercase; margin-top: 2px; }
  .business-card__contact { position: absolute; left: 18px; bottom: 14px; font-size: 7px; line-height: 1.4; }
</style>
</head>
<body>

  <section class="folder-cover">
    <div class="brand-lockup">
      <span class="brand-lockup__square"></span>
      <span class="brand-lockup__name">HEARTH &amp; TILE<br>CRAFTERS</span>
    </div>
  </section>

  <section class="brochure-page">
    <div class="brand-lockup">
      <span class="brand-lockup__square"></span>
      <span class="brand-lockup__name">HEARTH &amp; TILE<br>CRAFTERS</span>
    </div>
    <div class="hero-photo" role="img" aria-label="Modern kitchen with blue glass tile backsplash, steel range hood and white cabinets"></div>
    <div class="hero-band">SMART HOME TREND IN THE KITCHEN<br>AND ENJOY YOUR LIFE</div>
    <div class="thumb thumb--kitchen" role="img" aria-label="Dark wood kitchen with island and glass-front cabinets"></div>
    <div class="thumb thumb--bath" role="img" aria-label="Dark modern bathroom with floating vanity"></div>
    <div class="thumb thumb--room" role="img" aria-label="Bright remodeled interior"></div>
    <p class="brochure-page__url">www.hearthtilecrafters.com</p>
  </section>

  <section class="business-card">
    <p class="business-card__name">What is your name?</p>
    <p class="business-card__role">Project Manager</p>
    <p class="business-card__contact">515-482-7395<br>htcraftersmidwest@pinemail.net</p>
  </section>

</body>
</html>
```